GP Information brochure

we are looking for a designed brochure to send to doctors regarding our products and services. i have attached a very brief design and some information to start the design process.
I have also attached a previous flyer so that the theme and designs stay the same
please let me know if you require anything further
our slogan is: "Improving the quality of life for every individual"
Size: A4
general practitioners and allied health industry
Health And Wellness

```html
<!DOCTYPE html>
<html lang="en">
<head>
<meta charset="utf-8">
<title>Kinetra Health Club – Services Flyer</title>
<link rel="stylesheet" href="https://fonts.googleapis.com/css2?family=Megrim&family=Michroma&family=Open+Sans:wght@400;600;700&display=swap">
<style>
  :root {
    --page-bg: #e9e9ec;
    --body-blue-top: #4d5ea8;
    --body-blue-mid: #6a7cc4;
    --body-blue-low: #3c4b96;
    --deep-navy: #2b3573;
    --accent-orange: #e98a23;
    --ring-green: #5fa93a;
    --band-green: #8cc04a;
    --text-light: #eef1ff;
    --logo-blue: #243a8c;
    --paper: #f7f7f4;
    --paper-text: #3a3a3a;
    --badge-purple: #9a2f8a;
  }
  * { box-sizing: border-box; margin: 0; padding: 0; }
  html, body { width: 1200px; height: 960px; overflow: hidden; background: var(--page-bg); }
  .flyer {
    position: absolute; left: 285px; top: 30px; width: 630px; height: 900px;
    overflow: hidden;
    background: linear-gradient(180deg, var(--body-blue-top) 40%, var(--body-blue-mid) 60%, var(--body-blue-low) 100%);
    box-shadow: 0 6px 24px rgba(0,0,0,.18);
  }
  .hero-photo {
    position: absolute; left: 0; top: 0; width: 630px; height: 380px;
    background: radial-gradient(ellipse at 60% 40%, #8a5a45 0%, #4a2c25 45%, #1c1518 100%);
  }
  .hero-curve { position: absolute; left: 0; top: 310px; width: 630px; height: 90px; }
  .offer-title {
    position: absolute; left: 12px; top: 24px;
    font-family: "Megrim", sans-serif; color: #fff; font-size: 27px; line-height: 34px;
    text-transform: lowercase; letter-spacing: 1px;
  }
  .photo-ring {
    position: absolute; border-radius: 50%; border: 5px solid var(--ring-green);
    box-shadow: 0 4px 10px rgba(0,0,0,.35);
  }
  .ring-gym { left: 382px; top: 266px; width: 220px; height: 220px;
    background: radial-gradient(circle at 50% 40%, #b9cfcf 0%, #5f7a78 50%, #28352f 100%); }
  .ring-cycle { left: 438px; top: 468px; width: 182px; height: 182px;
    background: radial-gradient(circle at 50% 50%, #c9c4bb 0%, #7b6a5b 50%, #3d3a38 100%); }
  .services-heading {
    position: absolute; left: 95px; top: 372px;
    font-family: "Megrim", sans-serif; font-size: 34px; color: var(--accent-orange); text-transform: lowercase;
  }
  .services-intro {
    position: absolute; left: 30px; top: 414px; width: 340px;
    font-family: "Megrim", sans-serif; font-size: 19px; line-height: 26px; color: var(--text-light);
    text-transform: lowercase;
  }
  .service-arrows { position: absolute; left: 18px; top: 505px; width: 40px; height: 240px; }
  .service-list {
    position: absolute; left: 63px; top: 503px; list-style: none;
    font-family: "Megrim", sans-serif; font-size: 17px; line-height: 32.3px; color: var(--text-light);
    text-transform: lowercase; letter-spacing: 1px;
  }
  .service-list .spread { word-spacing: 14px; }
  .brand {
    position: absolute; left: 34px; top: 768px; display: flex; align-items: center; gap: 12px;
  }
  .brand-mark { width: 34px; height: 44px; border-radius: 6px; background: #2a9fd6; }
  .brand-name {
    font-family: "Michroma", sans-serif; font-size: 27px; color: var(--logo-blue); text-transform: lowercase;
  }
  .brand-tag {
    position: absolute; left: 80px; top: 804px; width: 170px;
    font-family: "Open Sans", sans-serif; font-size: 8px; color: var(--band-green);
    text-transform: uppercase; text-align: center; letter-spacing: 1px;
  }
  .rebates-band { position: absolute; left: 0; top: 836px; width: 300px; height: 44px; }
  .rebates-band-label {
    position: absolute; left: 46px; top: 844px;
    font-family: "Michroma", sans-serif; font-size: 25px; color: #fff; letter-spacing: 2px;
  }
  .footer-strip { position: absolute; left: 0; top: 880px; width: 630px; height: 20px; background: var(--deep-navy); }
  .rebates-card {
    position: absolute; left: 302px; top: 692px; width: 310px; height: 188px;
    background: var(--paper); box-shadow: 0 2px 8px rgba(0,0,0,.35);
    font-family: "Open Sans", sans-serif; color: var(--paper-text);
  }
  .rebates-card h2 {
    font-size: 12px; font-weight: 600; padding: 9px 0 2px 30px;
    border-bottom: 2px solid #4a7a4a; margin: 0 8px;
  }
  .rebates-badge {
    position: absolute; right: 6px; top: 2px; width: 88px; height: 30px;
    background: var(--badge-purple); clip-path: polygon(20% 0, 100% 0, 100% 100%, 20% 100%, 0 50%);
    color: #fff; font-size: 5px; font-weight: 700; line-height: 6px; text-align: center; padding: 3px 4px 0 18px;
  }
  .rebates-card p, .rebates-card li { font-size: 7.4px; line-height: 8px; }
  .rebates-card p { padding: 8px 20px 4px 32px; }
  .rebates-card ul { padding: 0 28px 0 46px; }
  .rebates-card li { margin-bottom: 5px; }
</style>
</head>
<body>
<main class="flyer">
  <div class="hero-photo" role="img" aria-label="Photo of a woman lifting a barbell on a weight bench in a gym"></div>
  <svg class="hero-curve" viewBox="0 0 630 90" aria-hidden="true">
    <path d="M0 40 Q300 -10 630 10 L630 90 L0 90 Z" fill="var(--accent-orange)"/>
    <path d="M0 58 Q300 8 630 22 L630 90 L0 90 Z" fill="var(--body-blue-top)"/>
  </svg>
  <h1 class="offer-title">Introductory Offers<br>Free 7 Days Trial</h1>

  <div class="photo-ring ring-gym" role="img" aria-label="Photo of the gym floor with weight machines"></div>
  <div class="photo-ring ring-cycle" role="img" aria-label="Photo of a spin class on exercise bikes"></div>

  <h2 class="services-heading">Our Services :</h2>
  <p class="services-intro">Our professional team is here to help you, no matter what your situation is.</p>

  <svg class="service-arrows" viewBox="0 0 40 240" aria-hidden="true" fill="none" stroke="var(--accent-orange)" stroke-width="1.6">
    <path d="M32 2 L4 20 L16 22 L20 32 Z"/>
    <path d="M32 36 L4 54 L16 56 L20 66 Z"/>
    <path d="M32 70 L4 88 L16 90 L20 100 Z"/>
    <path d="M32 104 L4 122 L16 124 L20 134 Z"/>
    <path d="M32 138 L4 156 L16 158 L20 168 Z"/>
    <path d="M32 172 L4 190 L16 192 L20 202 Z"/>
    <path d="M32 206 L4 224 L16 226 L20 236 Z"/>
  </svg>
  <ul class="service-list">
    <li class="spread">Chronic Disease Management</li>
    <li>(CDM) Plans</li>
    <li>Diabetes Programs: 1:1 &amp; Group</li>
    <li>Work Cover</li>
    <li>DVA</li>
    <li class="spread">National Disability Insurance</li>
    <li>Scheme (NDIS)</li>
  </ul>

  <div class="brand">
    <span class="brand-mark"></span>
    <span class="brand-name">Kinetra</span>
  </div>
  <div class="brand-tag">Health Club</div>

  <svg class="rebates-band" viewBox="0 0 300 44" aria-hidden="true">
    <polygon points="0,0 270,0 300,44 0,44" fill="var(--band-green)"/>
  </svg>
  <div class="rebates-band-label">RABATES</div>

  <section class="rebates-card">
    <h2>Rebates</h2>
    <div class="rebates-badge">Rebates for eligible Medicare, Health Fund and DVA Patients</div>
    <p>Individuals managing a current medical condition are advised to see their GP or specialist to obtain a referral to the Clinic. Referral form attached.</p>
    <ul>
      <li>Patients who have been referred by their GP and who have an Enhanced Primary Care Plan in place are able to claim Exercise Physiology and/or Physiotherapy Services through Medicare.</li>
      <li>DVA Gold Card holders are bulk-billed for all consultations.</li>
      <li>Private Patients - The large majority of private health funds provide rebates for Exercise Physiology and Physiotherapy services.</li>
      <li>Workers Compensation - Return to work rehabilitation services for injured workers.</li>
    </ul>
  </section>

  <div class="footer-strip"></div>
</main>
</body>
</html>
```